Unternehmen für Wimpernverlängerung & -lifting benötigt Flyer-Design
Zielgruppe
Wimpernverlängerung, Wimpernlifting, Permanent Make-Up, Microblading, BB Glow, Hyaluron Pen
Aufgabenstellung
es soll eine preisliste werden, ich möchte die preise selbst einsetzen
produkte:
Wimpernverlängerung:
Natural Look
Auffüllen bis 1-2 Wochen
Auffüllen bis 3-4 Wochen
Ab der 5. Woche Neupreis
Volumen Look
Wimpernlifting inkl. färben
Microblading
Permanent Make-Up:
Powder Brows
Powder Brows Combo (Härchen&Shading)
Wimpernkranzverdichtung
Lidstrich dekorativ
Aquarelle Lips
Lippen Vollschattierung
BB Glow
Hyaluron Pen
Termine nach Vereinbarung

```html
<!DOCTYPE html>
<html lang="de">
<head>
<meta charset="utf-8">
<title>Luma Lash – Preisliste</title>
<link rel="stylesheet" href="https://fonts.googleapis.com/css2?family=Crimson+Pro:wght@400;500&family=Montserrat:wght@300;400;500;600;700&display=swap">
<style>
  :root{
    --plum:#6b2f6e;
    --plum-dark:#5a2560;
    --pink:#ef9cc6;
    --pink-soft:#f6c6dc;
    --blush:#fcf0f5;
    --paper:#fff8fb;
    --text:#8a7a84;
    --stage:#e8e8e8;
  }
  *{box-sizing:border-box;margin:0;padding:0}
  html,body{width:750px;height:1200px;overflow:hidden;background:var(--stage)}
  body{position:relative;font-family:"Montserrat",sans-serif;color:var(--text)}
  .flyer{position:absolute;top:255px;width:345px;height:690px;overflow:hidden;
    background:linear-gradient(180deg,var(--blush),var(--paper) 60%,#fff);box-shadow:0 2px 10px rgba(0,0,0,.08)}
  .flyer--front{left:20px}
  .flyer--back{left:385px}
  .shapes{position:absolute;inset:0;width:345px;height:690px}
  .brand{position:absolute;left:26px;top:42px;font-family:"Montserrat",sans-serif;font-size:17px;
    font-weight:600;color:var(--plum);letter-spacing:1px}
  .badge{position:absolute;width:118px;height:118px;border-radius:50%;background:#fff;
    border:1.5px solid var(--plum);display:flex;align-items:center;justify-content:center}
  .badge__inner{width:102px;height:102px;border-radius:50%;background:var(--pink);
    display:flex;flex-direction:column;align-items:center;justify-content:center;color:var(--plum)}
  .badge__icon{width:20px;height:20px;margin-bottom:3px}
  .badge__label{font-size:11px;letter-spacing:1.5px;font-weight:400}
  .badge__phone{font-size:16px;font-weight:700;line-height:1.05;text-align:center;letter-spacing:-.3px}
  .section-head{position:absolute;left:0;right:0;height:30px}
  .section-head::before{content:"";position:absolute;left:0;right:0;top:15px;border-top:1px solid var(--pink-soft)}
  .pill{position:absolute;left:50%;transform:translateX(-50%);top:0;height:30px;padding:0 12px;border-radius:15px;
    background:var(--plum);border:2px solid #fff;outline:1px solid var(--pink-soft);
    font-family:"Crimson Pro",serif;color:#fff;font-size:16px;letter-spacing:.8px;line-height:26px;white-space:nowrap}
  .price-box{position:absolute;left:22px;right:22px;background:#fff;border:1px solid var(--pink-soft);
    padding:8px 14px 8px 28px}
  .price-box__tab{position:absolute;left:0;top:0;bottom:0;width:11px;background:var(--pink-soft);
    display:flex;align-items:center;justify-content:center}
  .price-box__tab span{transform:rotate(-90deg);white-space:nowrap;font-size:6px;color:var(--plum);letter-spacing:.3px}
  .row{display:flex;align-items:baseline;font-size:8.5px;line-height:14px;text-transform:uppercase;color:var(--text)}
  .row b{font-weight:600;color:#7a6773}
  .row__lead{flex:1;border-bottom:1px solid #cbbcc5;margin:0 3px;transform:translateY(-2px)}
  .row__price{font-weight:600;color:#6d5b67}
  .portrait{position:absolute;border-radius:50%;border:5px solid #fff;outline:1.5px solid var(--plum)}
  .portrait--person{left:24px;top:568px;width:114px;height:114px;
    background:radial-gradient(circle at 50% 40%,#6b4a50,#2b1f26 70%)}
  .portrait--studio{left:18px;top:556px;width:124px;height:124px;
    background:radial-gradient(circle at 50% 50%,#f4ece4,#d9c8b8 75%)}
  .tag{position:absolute;height:16px;padding:0 7px;border-radius:8px;background:var(--plum);border:1.5px solid #fff;
    outline:1px solid var(--pink-soft);font-family:"Crimson Pro",serif;font-size:9px;color:#fff;line-height:13px;
    letter-spacing:.4px;white-space:nowrap}
  .intro{position:absolute;left:176px;top:616px;width:160px}
  .intro__title{font-size:10.5px;font-weight:600;color:var(--plum);margin-bottom:6px}
  .intro__text{font-size:8px;line-height:10px;color:var(--text)}
  .contact{position:absolute;left:158px;top:592px;width:180px}
  .contact__title{font-size:10px;font-weight:700;color:var(--plum)}
  .contact__line{font-size:7.5px;color:var(--text);line-height:12px;display:flex;align-items:center;gap:4px}
  .contact__line strong{color:var(--plum);font-weight:600}
  .dot{width:9px;height:9px;border-radius:50%;background:var(--plum);display:inline-block;flex:none}
  .contact__social{display:flex;gap:14px;margin-top:2px}
  .web{margin-top:9px;height:18px;width:172px;border-radius:9px;background:var(--plum);color:#fff;
    font-family:"Crimson Pro",serif;font-size:11px;letter-spacing:.8px;text-align:center;line-height:18px}
</style>
</head>
<body>

<section class="flyer flyer--front">
  <svg class="shapes" viewBox="0 0 345 690">
    <defs>
      <linearGradient id="skin" x1="0" y1="0" x2="1" y2="1">
        <stop offset="0" stop-color="#f6e6dc"/><stop offset=".5" stop-color="#e9c7b4"/><stop offset="1" stop-color="#d9a993"/>
      </linearGradient>
    </defs>
    <path role="img" aria-label="Foto: Wimpernverlängerung mit Pinzette am Auge" d="M0 0H345V80C300 170 200 250 0 265Z" fill="url(#skin)"/>
    <path d="M0 265C200 250 300 170 345 80V96C300 190 200 262 0 282Z" fill="var(--pink)"/>
    <path d="M110 290C230 262 318 185 345 90V150C315 225 240 272 110 290Z" fill="var(--plum)"/>
    <path d="M0 690V648C50 615 130 592 230 585C140 602 60 640 20 690Z" fill="var(--plum)"/>
    <path d="M30 690C100 625 210 592 345 578V592C220 604 120 640 55 690Z" fill="var(--pink)"/>
  </svg>
  <div class="brand">LUMA LASH</div>

  <div class="badge" style="left:206px;top:160px">
    <div class="badge__inner">
      <svg class="badge__icon" viewBox="0 0 24 24"><path fill="var(--plum)" d="M6.6 10.8a15.1 15.1 0 0 0 6.6 6.6l2.2-2.2c.3-.3.7-.4 1-.2 1.1.4 2.3.6 3.6.6.6 0 1 .4 1 1V20c0 .6-.4 1-1 1A17 17 0 0 1 3 4c0-.6.4-1 1-1h3.5c.6 0 1 .4 1 1 0 1.3.2 2.5.6 3.6.1.3 0 .7-.2 1Z"/></svg>
      <div class="badge__label">TERMINE:</div>
      <div class="badge__phone">0151 480<br>73920</div>
    </div>
  </div>

  <div class="section-head" style="top:303px"><div class="pill">WIMPERNVERLÄNGERUNG:</div></div>

  <div class="price-box" style="top:352px;height:62px">
    <div class="price-box__tab"><span>NATURAL LOOK</span></div>
    <div class="row">Auffüllen | bis&nbsp;<b>1-2 Wochen</b><span class="row__lead"></span><span class="row__price">50,00€</span></div>
    <div class="row">Auffüllen | bis&nbsp;<b>3-4 Wochen</b><span class="row__lead"></span><span class="row__price">75,00€</span></div>
    <div class="row">Ab der&nbsp;<b>5. Woche</b>&nbsp;Neupreis<span class="row__lead"></span><span class="row__price">95,00€</span></div>
  </div>

  <div class="price-box" style="top:425px;height:62px">
    <div class="price-box__tab"><span>VOLUMEN LOOK</span></div>
    <div class="row">Auffüllen | bis&nbsp;<b>1-2 Wochen</b><span class="row__lead"></span><span class="row__price">50,00€</span></div>
    <div class="row">Auffüllen | bis&nbsp;<b>3-4 Wochen</b><span class="row__lead"></span><span class="row__price">75,00€</span></div>
    <div class="row">Ab der&nbsp;<b>5. Woche</b>&nbsp;Neupreis<span class="row__lead"></span><span class="row__price">95,00€</span></div>
  </div>

  <div class="price-box" style="top:497px;height:48px">
    <div class="price-box__tab"><span>SPECIALS</span></div>
    <div class="row"><b>Wimpernlifting</b>&nbsp;inkl. färben<span class="row__lead"></span><span class="row__price">50,00€</span></div>
    <div class="row"><b>Microblading</b><span class="row__lead"></span><span class="row__price">75,00€</span></div>
  </div>

  <div class="portrait portrait--person" role="img" aria-label="Porträtfoto der Inhaberin"></div>
  <div class="tag" style="left:84px;top:652px">MIRABEL TOSCH</div>

  <div class="intro">
    <div class="intro__title">ICH FREUE MICH AUF EUCH</div>
    <p class="intro__text">Mein Name ist Mirabel Tosch und ich bin seit 2014 zertifizierte Lash-Stylistin und seit 2017 Permanent Make-Up und Microblading Stylistin.</p>
  </div>
</section>

<section class="flyer flyer--back">
  <svg class="shapes" viewBox="0 0 345 690">
    <defs>
      <linearGradient id="face" x1="0" y1="0" x2="1" y2="1">
        <stop offset="0" stop-color="#f3f1f1"/><stop offset=".55" stop-color="#efd8cc"/><stop offset="1" stop-color="#e2bfae"/>
      </linearGradient>
    </defs>
    <path role="img" aria-label="Foto: Permanent Make-Up Behandlung der Augenbrauen" d="M0 0H345V40C300 140 200 205 0 215Z" fill="url(#face)"/>
    <path d="M0 215C200 205 300 140 345 40V58C300 160 200 218 0 232Z" fill="var(--pink)"/>
    <path d="M150 225C250 195 320 130 345 55V110C315 185 250 215 150 225Z" fill="var(--plum)"/>
    <path d="M0 690V660C40 625 110 585 200 578C120 600 50 640 15 690Z" fill="var(--plum)"/>
    <path d="M160 600C220 580 280 572 345 568V580C280 584 220 592 160 600Z" fill="var(--pink)"/>
  </svg>

  <div class="badge" style="left:206px;top:120px">
    <div class="badge__inner">
      <svg class="badge__icon" viewBox="0 0 24 24"><path fill="var(--plum)" d="M6.6 10.8a15.1 15.1 0 0 0 6.6 6.6l2.2-2.2c.3-.3.7-.4 1-.2 1.1.4 2.3.6 3.6.6.6 0 1 .4 1 1V20c0 .6-.4 1-1 1A17 17 0 0 1 3 4c0-.6.4-1 1-1h3.5c.6 0 1 .4 1 1 0 1.3.2 2.5.6 3.6.1.3 0 .7-.2 1Z"/></svg>
      <div class="badge__label">TERMINE:</div>
      <div class="badge__phone">0151 480<br>73920</div>
    </div>
  </div>

  <div class="section-head" style="top:262px"><div class="pill">PERMANENT MAKE-UP:</div></div>

  <div class="price-box" style="top:311px;height:102px;padding-top:10px">
    <div class="price-box__tab"><span>PERMANENT MAKE-UP</span></div>
    <div class="row">Powder Brows<span class="row__lead"></span><span class="row__price">50,00€</span></div>
    <div class="row">Powder Brows Combo (Härchen&amp;Shading)<span class="row__lead"></span><span class="row__price">75,00€</span></div>
    <div class="row">Wimpernkranzverdichtung<span class="row__lead"></span><span class="row__price">95,00€</span></div>
    <div class="row">Lidstrich dekorativ<span class="row__lead"></span><span class="row__price">50,00€</span></div>
    <div class="row">Aquarelle Lips<span class="row__lead"></span><span class="row__price">75,00€</span></div>
    <div class="row">Lippen Vollschattierung<span class="row__lead"></span><span class="row__price">95,00€</span></div>
  </div>

  <div class="section-head" style="top:435px"><div class="pill">WEITERE LEISTUNGEN:</div></div>

  <div class="price-box" style="top:484px;height:48px">
    <div class="price-box__tab"><span>SPECIALS</span></div>
    <div class="row">BB Glow<span class="row__lead"></span><span class="row__price">50,00€</span></div>
    <div class="row">Hyaluron Pen<span class="row__lead"></span><span class="row__price">75,00€</span></div>
  </div>

  <div class="portrait portrait--studio" role="img" aria-label="Foto des Studios"></div>
  <div class="tag" style="left:14px;top:561px">ICH FREUE MICH</div>

  <div class="contact">
    <div class="contact__title">TERMINE NACH VEREINBARUNG</div>
    <div class="contact__line"><strong>Mirabel Tosch</strong> | 87000 Lindenau/Berg</div>
    <div class="contact__line" style="margin-top:6px">
      <svg width="9" height="9" viewBox="0 0 24 24"><circle cx="12" cy="12" r="12" fill="var(--plum)"/><path fill="#fff" d="M9 8.5a8 8 0 0 0 6.5 6.5l1.2-1.2c.2-.2.4-.2.6-.1l1.7.6V16c0 .4-.3.7-.7.7A10 10 0 0 1 7.3 5.7c0-.4.3-.7.7-.7h1.7l.6 1.7c.1.2 0 .4-.1.6Z"/></svg>
      0151 480 73920 (für Terminanfragen)</div>
    <div class="contact__social">
      <div class="contact__line"><span class="dot"></span>luma_lash25</div>
      <div class="contact__line"><span class="dot"></span>luma_lash_de</div>
    </div>
    <div class="web">WWW.LUMA-LASH.DE</div>
  </div>
</section>

</body>
</html>
```